Contest - label design for a health related product with 4 color variations

Nuvera-Store (http://www.nuvera-store.example) is an online shop selling health related products and nutritional supplements, such as algae products, wheat grass and barley grass powder. These products have a positive impact on a person's health. Through Craft Huddle, we have designed already a logo for the shop and now we need to create labels that will be placed on a brown glass bottle (see attachment). The logo shall be used without the slogan 'One life. Live it healthy.' when creating the label.

Your job is to design a label with 4 color variations, blue, green, red and yellow. The measurements of the label is 80 mm x 173 mm, but please add 3 mm bleed to each side.

The information that has to go on the label can be taken from the attachment 'label information.pdf'. For the sake of communication, we will divide the label into 3 parts

- left
- middle
- right

The left part and the right part are fixed as this contains legal information. Please use easy to read fonts, non-serifed fonts, such as Arial, Verdana, Calibri. The left part contains a table and if Illustrator provides the possibility for tables, please use it as we need to be able to easily add and remove rows of the table.

The middle part contains the product description, the product quantity (i.e. 100 g), our logo without the slogan 'One live. Live it healthy.' and logos indicating the organic quality of the product (please see attachments). For the product name (i.e. QUB-Tangen) and the quantity (i.e. 100 Tabletten, 200 g) use the attached Lato font. Please note that the vertical position of our logo, the product name and the organic logos has NOT been set yet. You are free to position them where ever you feel in the middle part of the label.

Target Market(s)

Health concious people between 25 and 70

Industry/Entity Type

Health

Requirements
Must have
• - the attached logo without the slogan "One life...."
- the following attributes: healthy, joyful, vivid, lively, abstract, minimalistic
- colors that go along with our logo and the website www.nuvera-store.example
- all fonts need to be editable and not rendered
- the left part should have an editable table where we can add rows if necessary
- the attached font for product name and quantity
- 3 mm bleed on each side, so the final design is 6 mm wider and higher
- the final design will be in editable Illustrator files of a recent version.
Should not have
• - many overlaying, confusing lines or layers
- dark colors
- heavy appearance

```html
<!DOCTYPE html>
<html lang="de">
<head>
<meta charset="utf-8">
<title>Nuvera-Store Etiketten</title>
<link href="https://fonts.googleapis.com/css2?family=Lato:wght@300;400;700&display=swap" rel="stylesheet">
<style>
  :root {
    --green: #8cbf26;
    --green-light: #c9df7a;
    --green-pale: #e8f1c8;
    --green-title: #a6cd3f;
    --orange: #f3a512;
    --orange-light: #fbd35a;
    --orange-pale: #fdecb8;
    --text: #3a3a3a;
    --muted: #8a8a8a;
    --white: #ffffff;
  }
  * { box-sizing: border-box; margin: 0; padding: 0; }
  html, body { width: 1200px; height: 1180px; overflow: hidden; background: var(--white); }
  body { font-family: "Lato", Arial, sans-serif; color: var(--text); }

  .label {
    position: relative;
    width: 1200px;
    height: 575px;
    overflow: hidden;
    background: var(--white);
    --accent: var(--green);
    --accent-light: var(--green-light);
    --accent-pale: var(--green-pale);
    --title: var(--green-title);
  }
  .label + .label { margin-top: 30px; }
  .label--barley {
    --accent: var(--orange);
    --accent-light: var(--orange-light);
    --accent-pale: var(--orange-pale);
    --title: var(--orange);
  }

  .swoosh { position: absolute; inset: 0; width: 1200px; height: 575px; }
  .swoosh .band-pale { fill: var(--accent-pale); }
  .swoosh .band-light { fill: var(--accent-light); }
  .swoosh .band-main { fill: var(--accent); }

  /* left legal part */
  .legal { position: absolute; left: 14px; top: 14px; width: 310px; font-size: 12.5px; line-height: 1.35; }
  .legal b { font-weight: 700; }
  .ingredients { margin-bottom: 8px; }
  .nutrition { width: 100%; border-collapse: collapse; font-size: 12.5px; margin-bottom: 8px; }
  .nutrition th, .nutrition td { text-align: right; padding: 2px 0; }
  .nutrition th:first-child, .nutrition td:first-child { text-align: left; font-weight: 700; }
  .nutrition thead th { border-bottom: 1.5px solid var(--text); }
  .nutrition tbody tr:last-child td { border-bottom: 1.5px solid var(--text); }
  .distributor { position: absolute; left: 14px; top: 430px; font-size: 12.5px; line-height: 1.35; color: var(--muted); }

  /* middle part */
  .brand { position: absolute; left: 0; width: 1200px; top: 150px; display: flex; justify-content: center; align-items: center; gap: 14px; }
  .brand-dot { width: 34px; height: 34px; border-radius: 50%; background: var(--accent); }
  .brand-name { font-size: 34px; font-weight: 700; color: var(--accent); }
  .product-name { position: absolute; left: 0; width: 1200px; top: 270px; text-align: center; font-size: 70px; font-weight: 300; color: var(--title); }
  .label--barley .product-name { font-size: 58px; top: 280px; }
  .product-form { position: absolute; left: 0; width: 1200px; top: 360px; text-align: center; font-size: 30px; font-weight: 300; color: var(--muted); }
  .quantity { position: absolute; left: 470px; top: 488px; font-size: 40px; font-weight: 700; color: var(--white); }
  .badge { position: absolute; top: 484px; width: 58px; height: 54px; }
  .badge--organic { left: 600px; background: var(--white); border: 3px solid var(--accent); border-radius: 10px; }
  .badge--eu { left: 676px; background: var(--accent-light); border: 3px solid var(--white); }

  /* right part */
  .usage { position: absolute; left: 838px; top: 14px; width: 340px; font-size: 12.5px; line-height: 1.4; }
  .usage h2 { font-size: 13px; font-weight: 700; margin-bottom: 4px; }
  .usage p { margin-bottom: 10px; }
  .notes { list-style: none; margin-bottom: 10px; }
  .notes li { position: relative; padding-left: 12px; margin-bottom: 2px; }
  .notes li::before { content: ""; position: absolute; left: 0; top: 6px; width: 5px; height: 5px; background: var(--orange); }
</style>
</head>
<body>

<section class="label label--algae">
  <svg class="swoosh" viewBox="0 0 1200 575" aria-hidden="true">
    <path class="band-pale" d="M0,575 L0,470 C300,560 700,470 1200,250 L1200,575 Z"/>
    <path class="band-light" d="M0,575 L0,530 C350,580 750,470 1200,320 L1200,575 Z"/>
    <path class="band-main" d="M0,575 C300,575 520,470 1200,400 L1200,575 Z"/>
  </svg>

  <div class="legal">
    <p class="ingredients"><b>Zutaten:</b> QUB-Tangen (<i>AFA - Aphanizomenon Flos Aquae</i>) aus dem Klamath Lake, bei 37° C getrocknet.</p>
    <table class="nutrition">
      <thead><tr><th>Nährwertangaben</th><th>in 100 g</th><th>pro Kapsel</th></tr></thead>
      <tbody>
        <tr><td>Kohlenhydrate</td><td>xx g</td><td>xx g</td></tr>
        <tr><td>Fett</td><td>xx g</td><td>xx g</td></tr>
        <tr><td>Eiweiß</td><td>xx g</td><td>xx g</td></tr>
        <tr><td>Brennwert (kJ/kcal)</td><td>xx/xx</td><td>xx/xx</td></tr>
      </tbody>
    </table>
    <table class="nutrition">
      <thead><tr><th>Inhaltsstoffe</th><th>pro Kapsel</th><th>% RDA</th></tr></thead>
      <tbody><tr><td>Vitamin C</td><td>50,2 mg</td><td>50 %</td></tr></tbody>
    </table>
  </div>
  <p class="distributor">Vertrieb:<br>Mirabel Vane GmbH<br>Lindenhofgasse 14<br>1230 Wien<br>Österreich</p>

  <div class="brand"><span class="brand-dot"></span><span class="brand-name">Nuvera-Store</span></div>
  <h1 class="product-name">QUB-Tangen</h1>
  <p class="product-form">100 Tabletten</p>
  <p class="quantity">200 g ℮</p>
  <div class="badge badge--organic" role="img" aria-label="Bio-Siegel"></div>
  <div class="badge badge--eu" role="img" aria-label="EU-Bio-Siegel"></div>

  <div class="usage">
    <h2>Verzehrempfehlung:</h2>
    <p>3x täglich 3-5 Tabletten unzerkaut mit Wasser zu den Mahlzeiten einnehmen.</p>
    <h2>Hinweise:</h2>
    <ul class="notes">
      <li>Die angegebene Verzehrmenge sollte nicht überschritten werden.</li>
      <li>Nahrungsergänzungsmittel sind kein Ersatz für eine ausgewogene und abwechslungsreiche Ernährung.</li>
      <li>Das Produkt lichtgeschützt, verschlossen und außerhalb der Reichweite von kleinen Kindern aufbewahren.</li>
      <li>Während der Schwangerschaft und Stillzeiten sollte vor dem Verzehr von Nahrungsergänzungs­mitteln ein Arzt konsultiert werden.</li>
    </ul>
    <p>Mindestens haltbar bis: siehe Boden.</p>
  </div>
</section>

<section class="label label--barley">
  <svg class="swoosh" viewBox="0 0 1200 575" aria-hidden="true">
    <path class="band-pale" d="M0,575 L0,470 C300,560 700,470 1200,250 L1200,575 Z"/>
    <path class="band-light" d="M0,575 L0,530 C350,580 750,470 1200,320 L1200,575 Z"/>
    <path class="band-main" d="M0,575 C300,575 520,470 1200,400 L1200,575 Z"/>
  </svg>

  <div class="legal">
    <p class="ingredients"><b>Zutaten:</b> Lorem ipsum dolor sit, kisuaheli dors revlitz gofelt. Ipsum dolor sit.</p>
    <table class="nutrition">
      <thead><tr><th>Nährwertangaben</th><th>in 100 g</th><th>pro Kapsel</th></tr></thead>
      <tbody>
        <tr><td>Kohlenhydrate</td><td>xx g</td><td>xx g</td></tr>
        <tr><td>Fett</td><td>xx g</td><td>xx g</td></tr>
        <tr><td>Eiweiß</td><td>xx g</td><td>xx g</td></tr>
        <tr><td>Brennwert (kJ/kcal)</td><td>xx/xx</td><td>xx/xx</td></tr>
      </tbody>
    </table>
    <table class="nutrition">
      <thead><tr><th>Inhaltsstoffe</th><th>pro Kapsel</th><th>% RDA</th></tr></thead>
      <tbody><tr><td>Vitamin C</td><td>50,2 mg</td><td>50 %</td></tr></tbody>
    </table>
  </div>
  <p class="distributor">Vertrieb:<br>Mirabel Vane GmbH<br>Lindenhofgasse 14<br>1230 Wien<br>Österreich</p>

  <div class="brand"><span class="brand-dot"></span><span class="brand-name">Nuvera-Store</span></div>
  <h1 class="product-name">Gerstengraspulver</h1>
  <p class="quantity">200 g ℮</p>
  <div class="badge badge--organic" role="img" aria-label="Bio-Siegel"></div>
  <div class="badge badge--eu" role="img" aria-label="EU-Bio-Siegel"></div>

  <div class="usage">
    <h2>Verzehrempfehlung:</h2>
    <p>Lorem ipsum dolor sit, kisuaheli dors revlitz gofelt. Ipsum dolor sit.</p>
    <h2>Hinweise:</h2>
    <ul class="notes">
      <li>Die angegebene Verzehrmenge sollte nicht überschritten werden.</li>
      <li>Nahrungsergänzungsmittel sind kein Ersatz für eine ausgewogene und abwechslungsreiche Ernährung.</li>
      <li>Das Produkt lichtgeschützt, verschlossen und außerhalb der Reichweite von kleinen Kindern aufbewahren.</li>
      <li>Während der Schwangerschaft und Stillzeiten sollte vor dem Verzehr von Nahrungsergänzungs­mitteln ein Arzt konsultiert werden.</li>
    </ul>
    <p>Mindestens haltbar bis: siehe Boden.</p>
  </div>
</section>

</body>
</html>
```